Thornwell Building Company - advertisement poster

I am looking to print some canvas signs to advertise my general contracting company, Thornwell Building Company. The sign will measure 6' long x 3' high so the size should match that ratio. I already have a logo icon, which is the Letter 'A' and some trees that I would like to incorporate, see attached. I would also like the to have the following information listed:
1) phone number: 472-318-6095
2) email: thornwellbuildingcompany@mailvistra.net
3) website: thornwellbuildingcompany.com
4) Lic#5386204
5) I want to use this text: "BUILD WITH THE T-CREW!"

The ad should be relatively simple and clean. Black and Green are my company colors. I am open to creative ideas!

Target Market(s)

People looking to renovate their homes

Industry/Entity Type

Construction

Colors
59FF00
82FF00
B8FF75
E3FFCB
F4FFEA

Requirements
Must have
• Must have my company logo
Should not have
• No photos or complex graphics

```html
<!DOCTYPE html>
<html lang="en">
<head>
<meta charset="UTF-8">
<title>Thornwell Building Company – Sign</title>
<link rel="stylesheet" href="https://fonts.googleapis.com/css2?family=Montserrat:wght@600;700;800&family=Orbitron:wght@900&display=swap">
<style>
  :root {
    --page-bg: #e9edf1;
    --panel-left-top: #2b3342;
    --panel-left-bottom: #1c2129;
    --panel-right: #0c121a;
    --green: #5cb848;
    --white: #f2f2f2;
  }
  * { box-sizing: border-box; margin: 0; padding: 0; }
  html, body { width: 1200px; height: 900px; overflow: hidden; background: var(--page-bg); }
  .sign {
    position: absolute; left: 40px; top: 170px; width: 1120px; height: 560px;
    display: flex; box-shadow: 0 10px 30px rgba(0,0,0,.25);
    font-family: "Montserrat", sans-serif; color: var(--white);
  }
  .sign__info {
    width: 525px; position: relative;
    background: linear-gradient(160deg, var(--panel-left-top), var(--panel-left-bottom));
  }
  .brand {
    position: absolute; left: 40px; top: 50px; width: 300px;
    display: flex; flex-direction: column; align-items: center; gap: 16px;
  }
  .brand__mark { width: 70px; height: 70px; background: var(--green); }
  .brand__name {
    font-weight: 800; font-size: 24px; line-height: 1.15; text-align: center;
    text-transform: uppercase; letter-spacing: 1px; color: var(--white);
  }
  .brand__licence { font-weight: 700; font-size: 17px; }
  .contact {
    position: absolute; left: 40px; bottom: 45px; list-style: none;
    display: flex; flex-direction: column; gap: 20px;
  }
  .contact__item {
    display: flex; align-items: center; gap: 10px;
    font-weight: 700; font-size: 17px; letter-spacing: 1.6px;
  }
  .contact__icon { width: 18px; height: 18px; flex: none; }
  .sign__headline {
    flex: 1; background: var(--panel-right);
    display: flex; flex-direction: column; align-items: center; justify-content: space-between;
    padding: 42px 0 48px;
  }
  .headline__lead { font-weight: 800; font-size: 38px; letter-spacing: 7px; }
  .headline__brand { display: flex; flex-direction: column; align-items: center; gap: 18px; }
  .headline__mark { width: 150px; height: 150px; background: var(--green); }
  .headline__name { font-weight: 800; font-size: 34px; letter-spacing: 4px; text-transform: uppercase; }
  .headline__punch {
    font-family: "Orbitron", sans-serif; font-weight: 900; font-size: 88px;
    letter-spacing: 2px; line-height: 1;
  }
</style>
</head>
<body>
  <section class="sign">
    <div class="sign__info">
      <div class="brand">
        <span class="brand__mark"></span>
        <p class="brand__name">Thornwell<br>Building Company</p>
        <p class="brand__licence">Lic#5386204</p>
      </div>
      <ul class="contact">
        <li class="contact__item">
          <svg class="contact__icon" viewBox="0 0 24 24" fill="none" stroke="#5cb848" stroke-width="2"><circle cx="12" cy="12" r="10"/><path d="M8.5 7.5l2 2-1 1.5a7 7 0 0 0 3.5 3.5l1.5-1 2 2-1.5 1.5c-4 0-8-4-8-8z" fill="#5cb848" stroke="none"/></svg>
          472-318-6095
        </li>
        <li class="contact__item">
          <svg class="contact__icon" viewBox="0 0 24 24" fill="none" stroke="#5cb848" stroke-width="2"><rect x="2" y="5" width="20" height="14" rx="1"/><path d="M2 6l10 7 10-7"/></svg>
          thornwellbuildingcompany@mailvistra.net
        </li>
        <li class="contact__item">
          <svg class="contact__icon" viewBox="0 0 24 24" fill="none" stroke="#5cb848" stroke-width="2"><circle cx="12" cy="12" r="10"/><ellipse cx="12" cy="12" rx="4" ry="10"/><path d="M2 12h20"/></svg>
          thornwellbuildingcompany.com
        </li>
      </ul>
    </div>
    <div class="sign__headline">
      <p class="headline__lead">BUILD WITH THE</p>
      <div class="headline__brand">
        <span class="headline__mark"></span>
        <p class="headline__name">Thornwell</p>
      </div>
      <p class="headline__punch">T-CREW!</p>
    </div>
  </section>
</body>
</html>
```